Uni Camp Poster (Theme: Desert Oasis)

We require a poster design for our annual camp with the theme "desert oasis", please see the attached design brief for details.
We are the Coralline Fellowship (Cf), founded in 1996 at the Wexbridge Institute of Learning. As one of the largest social clubs at the Wexbridge Institute of Learning, Cf runs a variety of premier social and sporting events for University students.
Target Market(s)
18-19 year olds in Melbourne

```html
<!DOCTYPE html>
<html lang="en">
<head>
<meta charset="utf-8">
<title>Oasis – A Journey through the Sands</title>
<link href="https://fonts.googleapis.com/css2?family=Raleway:wght@500;700;800&family=Oswald:wght@400;500&family=Kalam:wght@400&display=swap" rel="stylesheet">
<style>
  :root {
    --mat: #595959;
    --sky: #f3eaea;
    --sand-deep: #e3bf2c;
    --sand: #eed35a;
    --sand-light: #f3e7a6;
    --foliage: #5f8a2a;
    --foliage-dark: #3e5f1c;
    --water: #8a9a55;
    --shore: #eedcb0;
    --olive: #434f17;
    --olive-text: #3b4712;
    --yellow: #f6ea14;
    --gold: #d9a91e;
    --white: #ffffff;
  }
  * { box-sizing: border-box; margin: 0; padding: 0; }
  html, body { width: 960px; height: 1200px; overflow: hidden; }
  body { background: var(--mat); position: relative; font-family: "Raleway", sans-serif; }

  .poster {
    position: absolute; left: 70px; top: 69px; width: 820px; height: 1062px;
    background: var(--sky); overflow: hidden;
  }
  .scene {
    position: absolute; left: 0; top: 150px; width: 100%; height: 912px;
    background: linear-gradient(to bottom,
      var(--sky) 0%,
      #eedfa8 7%,
      var(--sand-deep) 16%,
      var(--sand) 40%,
      var(--sand-light) 58%,
      #e8df9a 60%,
      var(--foliage) 64%,
      var(--foliage-dark) 73%,
      #7b8e3d 75%,
      var(--water) 80%,
      var(--foliage-dark) 88%,
      var(--shore) 95%,
      var(--shore) 100%);
  }

  .brand {
    position: absolute; left: 305px; top: 21px; width: 209px; height: 74px;
    background: var(--olive); display: flex; align-items: center; justify-content: center; gap: 9px;
  }
  .brand-mark { width: 13px; height: 13px; background: var(--white); }
  .brand-name {
    font-family: "Oswald", sans-serif; font-weight: 400; font-size: 22px; line-height: 1.0;
    color: var(--white); text-transform: uppercase; letter-spacing: 0.3px;
  }
  .presents {
    position: absolute; left: 0; width: 100%; top: 96px; text-align: center;
    font-family: "Kalam", cursive; font-size: 28px; color: var(--olive-text);
  }

  .title {
    position: absolute; left: 0; width: 100%; top: 198px; text-align: center;
    font-weight: 800; font-size: 210px; line-height: 1;
    letter-spacing: 6px; color: var(--gold);
    text-shadow: 2px 3px 0 #b98a10, 4px 6px 8px rgba(120, 85, 0, 0.35);
  }
  .subtitle {
    position: absolute; left: 0; width: 100%; top: 392px; text-align: center;
    font-weight: 800; font-size: 38px; line-height: 46px; color: var(--olive-text); letter-spacing: -0.3px;
  }
  .dates {
    position: absolute; left: 288px; top: 444px; width: 245px; height: 38px;
    border: 1.5px solid var(--olive-text); border-radius: 19px;
    display: flex; align-items: center; justify-content: center;
    font-weight: 800; font-size: 20px; color: var(--olive-text);
  }
  .dates sup { font-size: 11px; margin-right: 3px; }

  .prices { position: absolute; left: 203px; top: 493px; width: 413px; height: 43px; }
  .price-band { position: absolute; top: 0; height: 43px; background: var(--olive); display: flex; align-items: center; }
  .price-band.members { left: 0; width: 182px; clip-path: polygon(14px 0, 100% 0, 100% 100%, 0 100%); padding-left: 22px; }
  .price-band.guests { left: 231px; width: 182px; clip-path: polygon(0 0, 150px 0, 100% 100%, 0 100%); padding-left: 4px; }
  .price-join {
    position: absolute; left: 184px; top: 0; width: 45px; height: 43px; background: var(--olive);
    border: 1.5px solid var(--yellow); border-radius: 3px;
    display: flex; align-items: center; justify-content: center;
    font-weight: 800; font-size: 13px; color: var(--white);
  }
  .amount { font-weight: 800; font-size: 33px; color: var(--yellow); line-height: 1; display: flex; align-items: flex-end; }
  .amount .currency { font-size: 12px; font-weight: 500; margin-right: 1px; margin-bottom: 2px; }
  .audience { font-weight: 500; font-size: 11.5px; color: var(--white); line-height: 1.15; margin-left: 5px; }
</style>
</head>
<body>
  <main class="poster">
    <div class="scene" role="img" aria-label="Photograph of golden desert dunes with a camel caravan, green trees of an oasis reflected in still water, and birds flying in the pale sky"></div>

    <div class="brand">
      <span class="brand-mark"></span>
      <span class="brand-name">Coralline<br>Fellowship</span>
    </div>
    <p class="presents">presents</p>

    <h1 class="title">OASIS</h1>
    <h2 class="subtitle">A Journey through the Sands</h2>
    <p class="dates">11<sup>th</sup>&nbsp;to 13<sup>th</sup>&nbsp;March 2022</p>

    <div class="prices">
      <div class="price-band members">
        <span class="amount"><span class="currency">$</span>155</span>
        <span class="audience">for<br>Members</span>
      </div>
      <div class="price-join">AND</div>
      <div class="price-band guests">
        <span class="amount"><span class="currency">$</span>165</span>
        <span class="audience">for<br>Non-Members</span>
      </div>
    </div>
  </main>
</body>
</html>
```